Agricultural Commodities Specialist Needs a Business Card Design

Business owner Rob Hartwell, need a business card design for his company based in Brisbane, Australia called "RH Tradelink Pty Ltd".
Rob is an Agricultural Commodities Specialist:
-Specialising in Domestic and Export of Cotton,Cottonseed and Grains.
-Extensive experience in exporting into Asia especially China.
-Buyers agent for one of China's largest spinning mills.
-Capital raising from foreign investors into Australian agriculture.
-Agricultural marketing strategies for corporate and family farms.
-Importer of niche products from China.
-Array of contacts in agriculture and manufacturing in China.

Rob would like a professional business card with his company name "RH Tradelink" on the front of his business card - with contact details on the back. Preferably black and white colours.

CONTACT DETAILS THAT NEED TO BE INCLUDED:

Rob Hartwell
Mobile: 0431 275 604

Po Box 518
Elm Vale QLD 4187

Email: rob@rhtradelinkco.com
website: www.rhtradelinkc.com

```html
<!DOCTYPE html>
<html lang="en">
<head>
<meta charset="utf-8">
<title>RH Tradelink Pty Ltd – Business Card</title>
<link href="https://fonts.googleapis.com/css2?family=Open+Sans:wght@400;600&family=PT+Serif:wght@400&display=swap" rel="stylesheet">
<style>
  :root {
    --bg: #e6e6e4;
    --card-white: #ffffff;
    --ink: #1a1a1a;
    --rule: #555555;
    --icon-fill: #1a1a1a;
    --icon-glyph: #ffffff;
    --sky-top: #8fb8e6;
    --sky-low: #d9e6f2;
    --hills: #b49a5a;
    --field-light: #5fa52c;
    --field-dark: #2f6f16;
    --title-white: #ffffff;
  }
  * { margin: 0; padding: 0; box-sizing: border-box; }
  html, body {
    width: 1200px;
    height: 838px;
    overflow: hidden;
    background: var(--bg);
  }
  .canvas {
    width: 1200px;
    height: 838px;
    display: flex;
    align-items: center;
    justify-content: center;
    gap: 60px;
  }
  .card {
    width: 500px;
    height: 306px;
    position: relative;
    overflow: hidden;
    box-shadow: 0 2px 10px rgba(0,0,0,0.18);
  }

  /* Contact side */
  .card-back { background: var(--card-white); }
  .holder-name {
    position: absolute;
    left: 34px;
    top: 34px;
    font-family: "Open Sans", sans-serif;
    font-weight: 600;
    font-size: 22px;
    color: var(--ink);
  }
  .divider {
    position: absolute;
    left: 190px;
    top: 16px;
    bottom: 16px;
    width: 1px;
    background: var(--rule);
  }
  .contact-list {
    position: absolute;
    left: 212px;
    top: 40px;
    list-style: none;
    font-family: "PT Serif", serif;
    font-size: 17px;
    line-height: 30px;
    color: var(--ink);
  }
  .contact-row {
    display: flex;
    align-items: flex-start;
  }
  .contact-icon {
    width: 20px;
    height: 20px;
    margin-top: 5px;
    margin-right: 14px;
    flex: none;
  }
  .contact-row.indent { padding-left: 34px; }

  /* Brand side */
  .card-front { display: flex; align-items: center; justify-content: center; }
  .field-scene {
    position: absolute;
    inset: 0;
    background: linear-gradient(180deg,
      var(--sky-top) 0%,
      var(--sky-low) 18%,
      var(--hills) 24%,
      var(--field-light) 34%,
      var(--field-dark) 100%);
  }
  .company-title {
    position: relative;
    text-align: center;
    font-family: "Open Sans", sans-serif;
    font-weight: 400;
    font-size: 38px;
    line-height: 58px;
    color: var(--title-white);
    text-shadow: 0 1px 3px rgba(0,0,0,0.25);
  }
</style>
</head>
<body>
<main class="canvas">

  <section class="card card-back" aria-label="Card back with contact details">
    <h1 class="holder-name">Rob Hartwell</h1>
    <div class="divider"></div>
    <ul class="contact-list">
      <li class="contact-row">
        <svg class="contact-icon" viewBox="0 0 20 20" aria-hidden="true">
          <circle cx="10" cy="10" r="10" fill="var(--icon-fill)"/>
          <path d="M10 4.5a3.6 3.6 0 0 0-3.6 3.6c0 2.7 3.6 7 3.6 7s3.6-4.3 3.6-7A3.6 3.6 0 0 0 10 4.5z" fill="var(--icon-glyph)"/>
          <circle cx="10" cy="8.2" r="1.4" fill="var(--icon-fill)"/>
        </svg>
        <span>Po Box 518</span>
      </li>
      <li class="contact-row indent"><span>Elm Vale QLD 4187</span></li>
      <li class="contact-row">
        <svg class="contact-icon" viewBox="0 0 20 20" aria-hidden="true">
          <circle cx="10" cy="10" r="10" fill="var(--icon-fill)"/>
          <path d="M7 5l2 2.4-1.2 1.4c.7 1.5 1.8 2.6 3.3 3.3l1.4-1.2L15 13l-1 1.8c-4.6-.4-8.4-4.2-8.8-8.8z" fill="var(--icon-glyph)"/>
        </svg>
        <span>0431 275 604</span>
      </li>
      <li class="contact-row">
        <svg class="contact-icon" viewBox="0 0 20 20" aria-hidden="true">
          <circle cx="10" cy="10" r="10" fill="var(--icon-fill)"/>
          <rect x="5" y="6.5" width="10" height="7" fill="var(--icon-glyph)"/>
          <path d="M5 6.5l5 4 5-4" fill="none" stroke="var(--icon-fill)" stroke-width="1"/>
        </svg>
        <span>rob@rhtradelinkco.com</span>
      </li>
      <li class="contact-row">
        <svg class="contact-icon" viewBox="0 0 20 20" aria-hidden="true">
          <circle cx="10" cy="10" r="10" fill="var(--icon-fill)"/>
          <g fill="none" stroke="var(--icon-glyph)" stroke-width="1">
            <circle cx="10" cy="10" r="5"/>
            <ellipse cx="10" cy="10" rx="2.2" ry="5"/>
            <path d="M5 10h10M6 7.5h8M6 12.5h8"/>
          </g>
        </svg>
        <span>www.rhtradelinkco.com</span>
      </li>
    </ul>
  </section>

  <section class="card card-front" aria-label="Card front with company name">
    <div class="field-scene" role="img" aria-label="Photograph of rows of green crops stretching toward hills under a blue sky"></div>
    <h2 class="company-title">RH Tradelink<br>Pty Ltd</h2>
  </section>

</main>
</body>
</html>
```